Not-for-Profit Dog Breeding Association require interactive website

WREN is an Australian based Not-for-Profit Association established to support the pet industry. We aim to provide member services, as well as a public access portal for consumers. We are looking for an inspired web design team who can create a multi function website experience that meets the following three requirements.

1. Member portal for pet breeders
2. Consumer portal with various links and resources
3. Sales platform for breeders to list advertisements

10-12 Pages including the following functionality:
- Built on a quality content management system like wordpress
- Searchable Members register
- Public resources section
- Member log-in, registration and application templates
- Members only pages and resources
- Payment portal to process member payments
- Members Advertising Platform (ie. ability for members to list ads)
- Easy to use search and selling platform
- Links to Chatterly and Social Media
- Key Wording and Zorvex SEO
- Detailed editable Member Profiling
- About the Association
- Contact and Support

Logo and text content provided, additional creative brand styling required. Looking for outstanding quality and creativity from experienced website designers. Our aim is to lead the pet industry into a gold standard of care and operation and our website must reflect this level of quality.

```html
<!DOCTYPE html>
<html lang="en">
<head>
<meta charset="utf-8">
<title>WREN – Breeders Association for Registered Kennels</title>
<link href="https://fonts.googleapis.com/css2?family=Poppins:wght@400;500;600;700&display=swap" rel="stylesheet">
<style>
:root{
  --brown:#6b3a1d;
  --brown-dark:#3a1f10;
  --accent:#7d421a;
  --ink:#1d0f06;
  --cream:#faefe4;
  --hero-bg:#efd7c1;
  --tan:#c18b5c;
  --gold:#c98f55;
  --star:#f1a029;
  --text:#5a4a3f;
  --white:#ffffff;
}
*{box-sizing:border-box;margin:0;padding:0}
html,body{width:1200px;height:3793px;overflow:hidden}
body{font-family:'Poppins',sans-serif;background:var(--cream);color:var(--text);position:relative}
.abs{position:absolute}
.btn{position:absolute;display:flex;align-items:center;justify-content:center;color:var(--white);font-weight:600;text-transform:uppercase;background:linear-gradient(180deg,var(--brown) 0%,var(--tan) 100%);font-size:17px;letter-spacing:.2px}
.hl{color:var(--accent)}
h2.section-title{position:absolute;left:0;width:1200px;text-align:center;font-size:40px;font-weight:700;color:var(--ink);letter-spacing:.3px}

/* header */
.topbar{position:absolute;top:0;left:0;width:1200px;height:6px;background:var(--brown)}
.site-header{position:absolute;top:6px;left:0;width:1200px;height:117px;background:var(--cream)}
.logo{position:absolute;left:112px;top:32px;color:var(--brown)}
.logo-word{font-size:48px;font-weight:600;letter-spacing:14px;line-height:1}
.logo-sub{font-size:5.5px;font-weight:600;letter-spacing:.2px;margin-top:2px}
.nav{position:absolute;top:54px;left:376px;display:flex;gap:36px;font-size:14px;font-weight:500;color:#3b2a1f}
.quote-btn{left:925px;top:38px;width:162px;height:46px}

/* hero */
.hero{position:absolute;top:123px;left:0;width:1200px;height:634px;background:var(--hero-bg)}
.hero-side{position:absolute;left:770px;top:0;width:430px;height:634px;background:linear-gradient(135deg,#7d3f17,#a15a25 60%,#6e3414)}
.hero-title{position:absolute;left:112px;top:172px;font-size:37px;font-weight:700;line-height:45px;color:var(--ink)}
.hero-text{position:absolute;left:113px;top:328px;width:460px;font-size:14.5px;line-height:23px;color:#5b4a3c}
.start-btn{left:113px;top:410px;width:162px;height:45px}
.hero-photo{position:absolute;left:600px;top:77px;width:431px;height:511px;background:linear-gradient(160deg,#e8e6e0 0%,#d9a172 45%,#b8652a 70%,#3f5576 100%)}
.hero-frame{position:absolute;left:631px;top:48px;width:430px;height:420px;border:3px solid var(--white)}

/* about */
.about-img{position:absolute;left:75px;top:845px;width:550px;height:470px;background:radial-gradient(ellipse at 55% 50%,#e9d0b4 0%,#c8a585 45%,#dfe2e0 75%,rgba(250,239,228,0) 78%)}
.about-title{position:absolute;left:661px;top:866px;font-size:40px;font-weight:700;color:var(--ink)}
.about-text{position:absolute;left:661px;top:944px;width:425px;font-size:13px;line-height:22.5px;color:#5a4a3f}
.about-text p+p{margin-top:23px}
.learn-btn{left:661px;top:1290px;width:151px;height:45px;font-size:15px}

/* services */
.svc-card{position:absolute;overflow:hidden}
.svc-card .label{position:absolute;left:0;width:100%;text-align:center;color:var(--white);font-size:27px;font-weight:500}
.svc-card .frame{position:absolute;border:1.5px solid rgba(255,255,255,.85);border-radius:4px}
.svc-side{top:1610px;height:297px;border-radius:5px;background:linear-gradient(160deg,#3d4a52,#2b2b28 60%,#4a3422)}
.svc-main{left:406px;top:1573px;width:389px;height:369px;border-radius:5px;background:linear-gradient(150deg,#9a5a2c,#6b3a1b 55%,#4b2813);box-shadow:0 10px 28px rgba(0,0,0,.35)}

/* membership */
.plan{position:absolute;top:2163px;width:317px;height:404px;background:var(--white);box-shadow:0 2px 10px rgba(0,0,0,.06);text-align:center}
.plan-head{height:50px;background:var(--brown);color:var(--white);font-size:21px;font-weight:500;line-height:50px}
.plan-price{margin-top:25px;color:var(--accent);font-weight:600;font-size:34px;line-height:40px}
.plan-price sup{font-size:16px;vertical-align:14px;margin-right:4px}
.plan-price small{font-size:15px;font-weight:400;margin-left:6px}
.plan-tier{margin-top:6px;font-size:15.5px;font-weight:500;color:var(--accent)}
.plan ul{list-style:none;margin-top:20px;font-size:14px;line-height:28px;color:#6a5a4f}
.plan .btn{left:92px;top:387px;width:132px;height:36px;font-size:15px}

/* customers */
.customers{position:absolute;top:2665px;left:0;width:1200px;height:585px;background:linear-gradient(180deg,#c88d55,#d49a5c 50%,#c98a4e)}
.review{position:absolute;top:205px;width:290px}
.review p{margin-top:24px;font-size:13.5px;line-height:22.5px;color:#3a2718}
.review .who{margin-top:24px;font-size:15px;font-weight:600;color:var(--ink)}
.dots{position:absolute;top:465px;left:564px;display:flex;gap:4px}
.dots span{width:10px;height:10px;border-radius:50%;background:rgba(255,255,255,.75)}
.dots span.on{background:var(--white)}

/* footer */
.site-footer{position:absolute;top:3250px;left:0;width:1200px;height:543px;background:linear-gradient(180deg,#2e190c,#4b2914 70%,#5c3216)}
.foot-logo{position:absolute;left:112px;top:120px;font-size:74px;font-weight:600;letter-spacing:22px;color:var(--white);line-height:1}
.quick{position:absolute;left:492px;top:82px;color:var(--white)}
.quick h4{font-size:17px;font-weight:600;margin-bottom:10px}
.quick li{list-style:none;font-size:12.5px;line-height:22.5px}
.contact-title{position:absolute;left:112px;top:246px;font-size:21px;font-weight:600;color:var(--white)}
.ci{position:absolute;display:flex;gap:14px;align-items:center;color:var(--white)}
.ci .ic{width:48px;height:48px;border-radius:50%;background:var(--white);display:flex;align-items:center;justify-content:center}
.ci b{display:block;font-size:14.5px;font-weight:600;line-height:24px}
.ci span{font-size:13px;line-height:22px}
.copy{position:absolute;left:112px;top:470px;font-size:13px;color:var(--white)}
.social{position:absolute;left:930px;top:462px;display:flex;gap:16px}
.social span{width:28px;height:28px;border-radius:50%;background:var(--white)}

.inquiry{position:absolute;left:701px;top:3180px;width:387px;height:435px;background:var(--white);border-radius:8px}
.inquiry h3{position:absolute;top:42px;width:100%;text-align:center;font-size:29px;font-weight:700;color:var(--ink)}
.field{position:absolute;left:44px;width:300px;border:1.5px solid #cfcfcf;border-radius:4px;font-size:15px;color:#555;padding:0 22px;display:flex;align-items:center}
.send{left:132px;top:357px;width:125px;height:42px;font-size:16px}
</style>
</head>
<body>

<div class="topbar"></div>
<header class="site-header">
  <div class="logo">
    <div class="logo-word">WREN</div>
    <div class="logo-sub">BREEDERS ASSOCIATION FOR REGISTERED KENNELS INC</div>
  </div>
  <nav class="nav"><span>HOME</span><span>ABOUT US</span><span>SERVICES</span><span>MEMBERSHIP</span><span>CONTACT US</span></nav>
  <div class="btn quote-btn">Get a quote</div>
</header>

<section class="hero">
  <div class="hero-side" role="img" aria-label="Blurred close-up of a golden dog in warm brown tones"></div>
  <h1 class="hero-title">BREEDERS ASSOCIATION<br>FOR <span class="hl">REGISTERED</span><br><span class="hl">KENNELS</span></h1>
  <p class="hero-text">Promoting the health and welfare of all companion animals at every stage of their life, breeding and development.</p>
  <div class="btn start-btn">Get started</div>
  <div class="hero-photo" role="img" aria-label="Woman in an orange sweater kneeling forehead to forehead with a golden retriever"></div>
  <div class="hero-frame"></div>
</section>

<div class="about-img" role="img" aria-label="Young girl lying on a rug while a beagle puppy licks her cheek"></div>
<h2 class="about-title">ABOUT <span class="hl">WREN</span></h2>
<div class="about-text">
  <p>Lorem ipsum dolor sit amet, consectetur adipiscing elit, sed do eiusmod tempor incididunt ut labore et dolore magna aliqua. Quis ipsum suspendisse ultrices gravida. Risus commodo viverra maecenas accumsan lacus vel facilisis.</p>
  <p>Contrary to popular belief, Lorem Ipsum is not simply random text. It has roots in a piece of classical Latin literature from 45 BC, making it over 2000 years old. Harold Penwick, a Latin professor at Ashford Hill College in Virginia, looked up one of the more obscure Latin words, consectetur, from a Lorem Ipsum passage, and going through the cites of the word in classical literature, discovered the undoubtable source. Lorem Ipsum comes from sections 1.10.32 and 1.10.33 of "de Finibus Bonorum et Malorum" (The Extremes of Good and</p>
</div>
<div class="btn learn-btn">Learn more</div>

<h2 class="section-title" style="top:1465px">OUR <span class="hl">SERVICES</span></h2>
<div class="svc-card svc-side" style="left:120px;width:300px" role="img" aria-label="Dogs playing in an outdoor kennel yard">
  <div class="frame" style="left:16px;top:16px;width:290px;height:265px"></div>
  <div class="label" style="top:205px;left:-5px">Lorem Ipsum</div>
</div>
<div class="svc-card svc-side" style="left:780px;width:300px" role="img" aria-label="Dogs resting in front of a wooden kennel house">
  <div class="frame" style="left:-10px;top:16px;width:294px;height:265px"></div>
  <div class="label" style="top:205px;left:-6px">Lorem Ipsum</div>
</div>
<div class="svc-card svc-main" role="img" aria-label="Woman greeting a dog through kennel bars">
  <div class="frame" style="left:21px;top:21px;width:347px;height:327px"></div>
  <div class="label" style="top:242px">Lorem Ipsum</div>
</div>

<h2 class="section-title" style="top:2064px">OUR <span class="hl">MEMNBERSHIP</span></h2>

<div class="plan" style="left:101px">
  <div class="plan-head">PROVISIONAL BREEDER</div>
  <div class="plan-price"><sup>$</sup>9,99 / <small>Per Month</small></div>
  <div class="plan-tier">LIMITED MEMBERSHIP</div>
  <ul><li>Lorem Ipsum is simply text</li><li>Lorem Ipsum is simply</li><li>Lorem Ipsum</li><li>Podcasts</li><li>Lorem Ipsum is simply</li><li>Live podcast</li><li>Transformation</li></ul>
  <div class="btn">Sign up</div>
</div>
<div class="plan" style="left:441px">
  <div class="plan-head">REGISTERED KENNEL</div>
  <div class="plan-price"><sup>$</sup>19,99 / <small>Per Month</small></div>
  <div class="plan-tier">FULL MEMBERSHIP</div>
  <ul><li>Lorem Ipsum is simply text</li><li>Lorem Ipsum is simply</li><li>Lorem Ipsum</li><li>Podcasts</li><li>Lorem Ipsum is simply</li><li>Live podcast</li><li>Transformation</li></ul>
  <div class="btn">Sign up</div>
</div>
<div class="plan" style="left:781px">
  <div class="plan-head">KENNEL MASTER</div>
  <div class="plan-price"><sup>$</sup>49,99 / <small>Per Month</small></div>
  <div class="plan-tier">MEMBERSHIP WITH DISTINCTION</div>
  <ul><li>Lorem Ipsum is simply text</li><li>Lorem Ipsum is simply</li><li>Lorem Ipsum</li><li>Podcasts</li><li>Lorem Ipsum is simply</li><li>Live podcast</li><li>Transformation</li></ul>
  <div class="btn">Sign up</div>
</div>

<section class="customers" role="img" aria-label="Dogs among autumn leaves under a warm golden overlay">
  <h2 class="section-title" style="top:92px">OUR HAPPY CUSTOMERS</h2>
  <div class="review" style="left:134px">
    <svg width="100" height="18" viewBox="0 0 100 18"><g fill="#f1a029"><polygon points="9,1 11.4,6.5 17,7 12.7,10.8 14,16.5 9,13.5 4,16.5 5.3,10.8 1,7 6.6,6.5"/><polygon transform="translate(20)" points="9,1 11.4,6.5 17,7 12.7,10.8 14,16.5 9,13.5 4,16.5 5.3,10.8 1,7 6.6,6.5"/><polygon transform="translate(40)" points="9,1 11.4,6.5 17,7 12.7,10.8 14,16.5 9,13.5 4,16.5 5.3,10.8 1,7 6.6,6.5"/><polygon transform="translate(60)" points="9,1 11.4,6.5 17,7 12.7,10.8 14,16.5 9,13.5 4,16.5 5.3,10.8 1,7 6.6,6.5"/></g><polygon transform="translate(80)" fill="none" stroke="#f1a029" stroke-width="1.3" points="9,1 11.4,6.5 17,7 12.7,10.8 14,16.5 9,13.5 4,16.5 5.3,10.8 1,7 6.6,6.5"/></svg>
    <p>The standard chunk of Lorem Ipsum used since the 1500s is reproduced below for those interested. Sections 1.10.32 and 1.10.33 from "de Finibus Bonorum et Malorum" by Aurelian are also reproduced</p>
    <div class="who">Customer Name</div>
  </div>
  <div class="review" style="left:458px">
    <svg width="100" height="18" viewBox="0 0 100 18"><g fill="#f1a029"><polygon points="9,1 11.4,6.5 17,7 12.7,10.8 14,16.5 9,13.5 4,16.5 5.3,10.8 1,7 6.6,6.5"/><polygon transform="translate(20)" points="9,1 11.4,6.5 17,7 12.7,10.8 14,16.5 9,13.5 4,16.5 5.3,10.8 1,7 6.6,6.5"/><polygon transform="translate(40)" points="9,1 11.4,6.5 17,7 12.7,10.8 14,16.5 9,13.5 4,16.5 5.3,10.8 1,7 6.6,6.5"/><polygon transform="translate(60)" points="9,1 11.4,6.5 17,7 12.7,10.8 14,16.5 9,13.5 4,16.5 5.3,10.8 1,7 6.6,6.5"/></g><polygon transform="translate(80)" fill="none" stroke="#f1a029" stroke-width="1.3" points="9,1 11.4,6.5 17,7 12.7,10.8 14,16.5 9,13.5 4,16.5 5.3,10.8 1,7 6.6,6.5"/></svg>
    <p>The standard chunk of Lorem Ipsum used since the 1500s is reproduced below for those interested. Sections 1.10.32 and 1.10.33 from "de Finibus Bonorum et Malorum" by Aurelian are also reproduced</p>
    <div class="who">Customer Name</div>
  </div>
  <div class="review" style="left:782px">
    <svg width="100" height="18" viewBox="0 0 100 18"><g fill="#f1a029"><polygon points="9,1 11.4,6.5 17,7 12.7,10.8 14,16.5 9,13.5 4,16.5 5.3,10.8 1,7 6.6,6.5"/><polygon transform="translate(20)" points="9,1 11.4,6.5 17,7 12.7,10.8 14,16.5 9,13.5 4,16.5 5.3,10.8 1,7 6.6,6.5"/><polygon transform="translate(40)" points="9,1 11.4,6.5 17,7 12.7,10.8 14,16.5 9,13.5 4,16.5 5.3,10.8 1,7 6.6,6.5"/><polygon transform="translate(60)" points="9,1 11.4,6.5 17,7 12.7,10.8 14,16.5 9,13.5 4,16.5 5.3,10.8 1,7 6.6,6.5"/></g><polygon transform="translate(80)" fill="none" stroke="#f1a029" stroke-width="1.3" points="9,1 11.4,6.5 17,7 12.7,10.8 14,16.5 9,13.5 4,16.5 5.3,10.8 1,7 6.6,6.5"/></svg>
    <p>The standard chunk of Lorem Ipsum used since the 1500s is reproduced below for those interested. Sections 1.10.32 and 1.10.33 from "de Finibus Bonorum et Malorum" by Aurelian are also reproduced</p>
    <div class="who">Customer Name</div>
  </div>
  <div class="dots"><span></span><span></span><span class="on"></span><span></span><span></span></div>
</section>

<footer class="site-footer">
  <div class="foot-logo">WREN</div>
  <div class="quick">
    <h4>QUICK LINKS</h4>
    <ul><li>HOME</li><li>ABOUT US</li><li>OUR SERVICES</li><li>MEMBERSHIP</li><li>CONTACT US</li></ul>
  </div>
  <div class="contact-title">CONTACT INFO</div>
  <div class="ci" style="left:112px;top:313px">
    <div class="ic"><svg width="20" height="20" viewBox="0 0 24 24"><path fill="#6b3a1d" d="M6.6 10.8a15 15 0 0 0 6.6 6.6l2.2-2.2c.3-.3.7-.4 1-.2 1.1.4 2.3.6 3.6.6.6 0 1 .4 1 1V20c0 .6-.4 1-1 1A17 17 0 0 1 3 4c0-.6.4-1 1-1h3.5c.6 0 1 .4 1 1 0 1.3.2 2.5.6 3.6.1.3 0 .7-.2 1z"/></svg></div>
    <div><b>Phone Number</b><span>+1 555 0142 778</span></div>
  </div>
  <div class="ci" style="left:112px;top:381px">
    <div class="ic"><svg width="20" height="16" viewBox="0 0 20 16"><rect x="1" y="1" width="18" height="14" rx="2" fill="#6b3a1d"/><path d="M2 3l8 6 8-6" stroke="#fff" stroke-width="1.6" fill="none"/></svg></div>
    <div><b>Email</b><span>info@wrenconstitution.org</span></div>
  </div>
  <div class="ci" style="left:430px;top:313px">
    <div class="ic"><svg width="18" height="22" viewBox="0 0 18 22"><path fill="#6b3a1d" d="M9 0a8 8 0 0 0-8 8c0 6 8 14 8 14s8-8 8-14a8 8 0 0 0-8-8z"/><circle cx="9" cy="8" r="3" fill="#fff"/></svg></div>
    <div><span style="display:block;line-height:26px">72 Holloway Lane</span><span>Location 40218</span></div>
  </div>
  <div class="ci" style="left:430px;top:381px">
    <div class="ic"><svg width="20" height="18" viewBox="0 0 20 18"><rect x="1" y="5" width="18" height="12" rx="2" fill="#6b3a1d"/><path d="M7 5V3a1 1 0 0 1 1-1h4a1 1 0 0 1 1 1v2" stroke="#6b3a1d" stroke-width="1.8" fill="none"/><path d="M1 10h18" stroke="#fff" stroke-width="1.3"/></svg></div>
    <div><b>Working Hours</b><span>Mon – Fri: 9:00 – 5:00</span></div>
  </div>
  <div class="copy">Copyright © 2022 Wren Constitution . All Right Reserved</div>
  <div class="social" aria-label="Social links: Chatterly and other networks"><span></span><span></span><span></span><span></span></div>
</footer>

<div class="inquiry">
  <h3>QUICK <span class="hl">INQUIRY</span></h3>
  <div class="field" style="top:90px;height:52px">Your Name*</div>
  <div class="field" style="top:157px;height:52px">Email Address*</div>
  <div class="field" style="top:224px;height:112px;align-items:flex-start;padding-top:16px">Your Message Here .....</div>
  <div class="btn send">Send now</div>
</div>

</body>
</html>
```